Personal Training Studio business cards

Black logo on front. Also need: Loralie Fenwright Master Trainer, Phone: 0487315620 on the front.
On the back want the white logo and also want 10 stars or similar that can be stamped when attended Studio. The 10th start to have "Free" written under it.
Also want a line to write an appointment date and time on it.

```html
<!DOCTYPE html>
<html lang="en">
<head>
<meta charset="utf-8">
<title>Corewell Studio – Business Card</title>
<link rel="stylesheet" href="https://fonts.googleapis.com/css2?family=Poppins:wght@400;600;700&family=Open+Sans:wght@400;600&display=swap">
<style>
  :root {
    --page: #5e5e5e;
    --navy-deep: #01141f;
    --navy-glow: #1c3b4d;
    --purple: #6b45a6;
    --green: #8cc63f;
    --white: #ffffff;
    --card-white: #f7f7f7;
    --ink: #333333;
  }
  * { box-sizing: border-box; margin: 0; padding: 0; }
  html, body { width: 1200px; height: 1200px; overflow: hidden; }
  body {
    background: var(--page);
    font-family: "Poppins", sans-serif;
    position: relative;
  }
  .card {
    position: absolute;
    left: 120px;
    width: 960px;
    height: 540px;
    border-radius: 22px;
    box-shadow: 0 10px 24px rgba(0,0,0,0.35);
    overflow: hidden;
  }
  /* Front */
  .card--front {
    top: 40px;
    background: radial-gradient(circle at 58% 62%, var(--navy-glow) 0%, #0b2433 30%, var(--navy-deep) 70%);
    display: flex;
    align-items: center;
    padding: 0 60px 40px 80px;
  }
  .brand {
    width: 350px;
    display: flex;
    align-items: center;
    gap: 14px;
  }
  .brand__dot {
    width: 22px; height: 22px;
    border-radius: 50%;
    background: var(--white);
    flex: none;
  }
  .brand__name {
    font-weight: 600;
    font-size: 34px;
    line-height: 1;
    color: var(--white);
    white-space: nowrap;
  }
  .divider {
    width: 2px;
    height: 150px;
    background: rgba(255,255,255,0.75);
    margin: 0 40px 0 20px;
    flex: none;
  }
  .contact__name {
    font-weight: 700;
    font-size: 36px;
    color: var(--white);
    line-height: 1.15;
    white-space: nowrap;
  }
  .contact__role {
    font-size: 26px;
    color: var(--green);
    margin-top: 4px;
  }
  .contact__phone {
    display: flex;
    align-items: center;
    gap: 10px;
    font-size: 26px;
    letter-spacing: 2px;
    color: var(--white);
    margin-top: 14px;
  }
  /* Back */
  .card--back {
    top: 620px;
    background: radial-gradient(circle at 50% 55%, #ebebeb 0%, var(--card-white) 65%);
    display: grid;
    grid-template-columns: repeat(5, 1fr);
    grid-template-rows: repeat(2, 1fr);
    padding: 30px 30px 20px;
  }
  .stamp {
    position: relative;
    display: flex;
    flex-direction: column;
    align-items: center;
  }
  .stamp__number {
    position: absolute;
    left: 10px;
    top: 0;
    width: 28px; height: 28px;
    border-radius: 50%;
    background: var(--purple);
    color: var(--white);
    font-size: 15px;
    font-weight: 600;
    display: flex; align-items: center; justify-content: center;
  }
  .stamp__star { width: 118px; height: 112px; margin-top: 2px; }
  .stamp__label {
    font-family: "Open Sans", sans-serif;
    font-size: 19px;
    color: var(--ink);
    margin-top: 2px;
  }
  .stamp__line {
    width: 148px;
    height: 2px;
    background: var(--purple);
    margin-top: 30px;
  }
  .stamp__line + .stamp__line { margin-top: 36px; }
  .stamp__free {
    font-family: "Open Sans", sans-serif;
    font-weight: 600;
    font-size: 13px;
    fill: #555;
  }
</style>
</head>
<body>
  <svg width="0" height="0" style="position:absolute">
    <defs>
      <symbol id="star-outline" viewBox="0 0 100 96">
        <polygon points="50,3 62,36 97,37 69,58 79,92 50,72 21,92 31,58 3,37 38,36"
                 fill="none" stroke="#8cc63f" stroke-width="2.6" stroke-linejoin="miter"/>
      </symbol>
    </defs>
  </svg>

  <section class="card card--front">
    <div class="brand">
      <span class="brand__dot"></span>
      <span class="brand__name">Corewell Studio</span>
    </div>
    <div class="divider"></div>
    <div class="contact">
      <p class="contact__name">Loralie Fenwright</p>
      <p class="contact__role">Master Trainer</p>
      <p class="contact__phone">
        <svg width="20" height="26" viewBox="0 0 20 26" aria-hidden="true">
          <rect x="2" y="2" width="16" height="22" rx="3" fill="none" stroke="#fff" stroke-width="2.4"/>
          <line x1="6" y1="19" x2="14" y2="19" stroke="#fff" stroke-width="2"/>
        </svg>
        0487315620
      </p>
    </div>
  </section>

  <section class="card card--back">
    <div class="stamp"><span class="stamp__number">1</span><svg class="stamp__star"><use href="#star-outline"/></svg><span class="stamp__label">Appointment</span><span class="stamp__line"></span><span class="stamp__line"></span></div>
    <div class="stamp"><span class="stamp__number">2</span><svg class="stamp__star"><use href="#star-outline"/></svg><span class="stamp__label">Appointment</span><span class="stamp__line"></span><span class="stamp__line"></span></div>
    <div class="stamp"><span class="stamp__number">3</span><svg class="stamp__star"><use href="#star-outline"/></svg><span class="stamp__label">Appointment</span><span class="stamp__line"></span><span class="stamp__line"></span></div>
    <div class="stamp"><span class="stamp__number">4</span><svg class="stamp__star"><use href="#star-outline"/></svg><span class="stamp__label">Appointment</span><span class="stamp__line"></span><span class="stamp__line"></span></div>
    <div class="stamp"><span class="stamp__number">5</span><svg class="stamp__star"><use href="#star-outline"/></svg><span class="stamp__label">Appointment</span><span class="stamp__line"></span><span class="stamp__line"></span></div>
    <div class="stamp"><span class="stamp__number">6</span><svg class="stamp__star"><use href="#star-outline"/></svg><span class="stamp__label">Appointment</span><span class="stamp__line"></span><span class="stamp__line"></span></div>
    <div class="stamp"><span class="stamp__number">7</span><svg class="stamp__star"><use href="#star-outline"/></svg><span class="stamp__label">Appointment</span><span class="stamp__line"></span><span class="stamp__line"></span></div>
    <div class="stamp"><span class="stamp__number">8</span><svg class="stamp__star"><use href="#star-outline"/></svg><span class="stamp__label">Appointment</span><span class="stamp__line"></span><span class="stamp__line"></span></div>
    <div class="stamp"><span class="stamp__number">9</span><svg class="stamp__star"><use href="#star-outline"/></svg><span class="stamp__label">Appointment</span><span class="stamp__line"></span><span class="stamp__line"></span></div>
    <div class="stamp"><span class="stamp__number">10</span>
      <svg class="stamp__star" viewBox="0 0 100 96">
        <use href="#star-outline"/>
        <text class="stamp__free" x="50" y="60" text-anchor="middle">FREE</text>
      </svg>
      <span class="stamp__label">Appointment</span><span class="stamp__line"></span><span class="stamp__line"></span></div>
  </section>
</body>
</html>
```